Walk Through the Fog Step out, step up and into your best performance

BRIEF FOR BOOK FRONT COVER

• It needs to be iconic
• It needs to be a ‘clean’ design
• Needs to be seen on a bookshelf in an airport from 50 feet away
• No stick like figures/cartoon style or cutesy design
• The book appeals to both male and female readers
• This is a cross over book and covers a couple of genres like Marcus Televan’s book The Engine of Routine or Odile Fenwick’s Leaping Boldly. So it is primarily about taking better care of yourself personally, professionally and will appeal to those in business.
• The idea that a personal enriching life feeds into an engaged performer on the job – they feed off each other leading to increased engagement, productivity and fulfillment
• The dance analogy means that you are not sitting on the sidelines of your life or business
• It is laced with inspiring real life case studies
• Positioning of the book: People facing adversity and still come through better than ever and better equipped to what comes next.
• Want a cover that would attract a Pinnacle 50 CEO to buy the book for his staff
• My name as the author should be across the bottom KESTA VOREHAM MBA MCC
Updates

Project Deadline Extended Reason: A big thank you for all the designers who submitted a cover design and I have been spoilt for choiceI need to finalize the copy on the book cover and hence the need for an extension of time.Thanks for your understanding.Kesta Added Sunday, September 18, 2016

Target Market(s)

Professionals in the age group 25 - 55

Industry/Entity Type

Airport

Contact Information for Business Card

basic information and a very clean look

Logo Text

probably book title more important that it can be seen clearly when the size is reduced to a small size e.g. if sponsoring an event

Number of Pages Required

5+ page

Font styles to use
Sans Serif

Colors
ec1f27
f37122
abd037

Requirements
Must have
• info already provided

```html
<!DOCTYPE html>
<html lang="en">
<head>
<meta charset="utf-8">
<title>Walk Through the Fog — Front Cover</title>
<link rel="stylesheet" href="https://fonts.googleapis.com/css2?family=Oswald:wght@500&family=Archivo+Black&family=Josefin+Sans:wght@600&display=swap">
<style>
  :root {
    --backdrop: #a9a79d;
    --cover-black: #000000;
    --silver-light: #f2f2f2;
    --silver-mid: #bdbdbd;
    --silver-dark: #7d7d7d;
    --accent-lime: #d7e21c;
    --author-pink: #ec2a4f;
  }
  html, body {
    margin: 0;
    padding: 0;
    width: 1200px;
    height: 900px;
    overflow: hidden;
    background: var(--backdrop);
  }
  .book-cover {
    position: absolute;
    left: 338px;
    top: 92px;
    width: 533px;
    height: 689px;
    background: var(--cover-black);
    overflow: hidden;
  }
  .cover-artwork {
    position: absolute;
    left: 0;
    top: 0;
    width: 533px;
    height: 363px;
    background:
      radial-gradient(ellipse 40% 70% at 50% 20%, rgba(255,255,255,0.45), transparent 70%),
      radial-gradient(ellipse 30% 40% at 25% 45%, rgba(230,90,60,0.35), transparent 70%),
      radial-gradient(ellipse 30% 40% at 75% 45%, rgba(80,140,220,0.35), transparent 70%),
      radial-gradient(ellipse 50% 30% at 50% 80%, rgba(200,120,60,0.3), transparent 70%),
      linear-gradient(180deg, #2a211c 0%, #1a1512 65%, #000 100%);
  }
  .title-block {
    position: absolute;
    left: 0;
    top: 412px;
    width: 533px;
  }
  .title-top {
    display: flex;
    justify-content: center;
    align-items: stretch;
    margin-left: 40px;
  }
  .silver-text {
    background: linear-gradient(180deg, var(--silver-light) 0%, var(--silver-mid) 45%, var(--silver-dark) 70%, var(--silver-mid) 100%);
    -webkit-background-clip: text;
    background-clip: text;
    color: transparent;
  }
  .title-main {
    font-family: "Oswald", sans-serif;
    font-weight: 500;
    font-size: 124px;
    line-height: 92px;
    height: 92px;
    letter-spacing: -1px;
    padding-top: 2px;
  }
  .title-linker {
    writing-mode: vertical-rl;
    font-family: "Oswald", sans-serif;
    font-weight: 500;
    font-size: 14px;
    letter-spacing: 0.5px;
    color: var(--accent-lime);
    margin-left: 4px;
    height: 92px;
    text-align: center;
    line-height: 14px;
  }
  .title-end {
    display: block;
    font-family: "Archivo Black", sans-serif;
    font-size: 78px;
    line-height: 64px;
    letter-spacing: 4px;
    text-align: center;
    transform: skewX(-22deg);
    margin-left: -20px;
    margin-top: 2px;
  }
  .author {
    position: absolute;
    left: 0;
    top: 630px;
    width: 533px;
    text-align: center;
    font-family: "Josefin Sans", sans-serif;
    font-weight: 600;
    font-size: 21px;
    letter-spacing: 2px;
    color: var(--author-pink);
  }
</style>
</head>
<body>
  <main class="book-cover">
    <div class="cover-artwork" role="img" aria-label="Abstract artwork of glowing multicoloured droplets on black, mirrored around a bright horizon line"></div>
    <h1 class="title-block">
      <span class="title-top">
        <span class="title-main silver-text">WALK</span>
        <span class="title-linker">THROUGH THE</span>
      </span>
      <span class="title-end silver-text">FOG</span>
    </h1>
    <p class="author">KESTA VOREHAM MBA MCC</p>
  </main>
</body>
</html>
```